Direct mailing postcard for Real Estate Photography marketing

I am looking for an oversized postcard for direct mail marketing to Real Estate agents and brokers offices. Something that will stand out and be eye catching if seen sitting on a desk or counter by other agents.

Target Market(s)

Real Estate agents and brokers for listings

Industry/Entity Type

Photographer

Other font styles liked:
• Leave this up to the designer. Should match logo

Colors
fece3e
fbed22
33a6d7
3276b5

```html
<!DOCTYPE html>
<html lang="en">
<head>
<meta charset="utf-8">
<title>Coral Coast Imaging – Postcard</title>
<link href="https://fonts.googleapis.com/css2?family=Oswald:wght@500;600&family=Roboto+Condensed:ital,wght@0,400;0,700;1,400&display=swap" rel="stylesheet">
<style>
  :root{
    --orange:#f7941d;
    --orange-deep:#f08a12;
    --ink:#111;
    --white:#fff;
    --page:#e4e5e7;
    --sky:#6fa6d8;
    --water:#3f7fae;
    --interior:#d9dcdf;
    --seal:#c9ccd2;
  }
  *{box-sizing:border-box;margin:0;padding:0}
  html,body{width:1200px;height:1000px;overflow:hidden}
  body{background:var(--page);position:relative;font-family:"Roboto Condensed",Arial,sans-serif;color:var(--ink)}
  .card{position:absolute;top:315px;width:570px;height:370px;background:var(--white);overflow:hidden;box-shadow:0 2px 6px rgba(0,0,0,.18)}
  .card--front{left:28px}
  .card--back{left:612px}

  /* front */
  .hero-photo{position:absolute;left:0;top:0;width:570px;height:232px;
    background:linear-gradient(180deg,#f1f1f1 0%,var(--sky) 22%,#8fb9dd 40%,var(--water) 55%,#9eb78b 68%,var(--interior) 80%,#cfd2d4 100%)}
  .hero-rule{position:absolute;left:0;top:232px;width:570px;height:4px;background:var(--orange)}
  .inset-photo{position:absolute;left:337px;top:150px;width:216px;height:146px;border:3px solid var(--orange);
    background:linear-gradient(180deg,#eceeef 0%,#c9ced2 45%,#3d8f9e 62%,#b8bdc1 80%,#9da2a6 100%)}
  .headline{position:absolute;left:20px;top:246px;font-family:"Oswald",Arial,sans-serif;font-weight:600;font-size:23px;line-height:26px;letter-spacing:-.2px;text-transform:uppercase}
  .brand{position:absolute;display:flex;align-items:center;gap:8px;white-space:nowrap}
  .brand__mark{width:30px;height:30px;border-radius:50%;background:var(--orange);flex:none}
  .brand__name{font-weight:700;color:var(--orange-deep);text-transform:uppercase;letter-spacing:.4px;line-height:1.05}
  .card--front .brand{left:30px;top:312px}
  .card--front .brand__name{font-size:17px}
  .contact{position:absolute;right:20px;text-align:right;font-size:13px;line-height:19px;white-space:nowrap}
  .card--front .contact{top:318px}
  .contact__web{color:var(--ink)}

  /* back */
  .back-band{position:absolute;left:0;top:0;width:570px;height:162px;background:var(--orange)}
  .back-band-ext{position:absolute;left:0;top:162px;width:378px;height:44px;background:var(--orange)}
  .stamp{position:absolute;left:478px;top:10px;width:80px;height:80px;background:var(--white);border:1px solid #555}
  .gallery-photo{position:absolute;top:14px;width:96px;height:140px;border:2px solid #f3d7b0}
  .gallery-photo--one{left:262px;background:linear-gradient(180deg,#efe9e1,#6b4a36 40%,#a07a5b 70%,#e9e5df)}
  .gallery-photo--two{left:364px;background:linear-gradient(180deg,#dfe8f0,#f4f2ee 35%,#5a3a2a 65%,#ece8e2)}
  .intro{position:absolute;left:19px;top:16px;width:238px;font-size:12.5px;line-height:15px}
  .service{position:absolute;left:19px;top:84px;width:238px;font-size:12.5px;line-height:15px}
  .service__title{font-family:"Oswald",Arial,sans-serif;font-weight:500;font-size:13px;text-transform:uppercase;margin-bottom:1px}
  .service__list{list-style:none;margin-top:1px}
  .service__list li{display:flex;align-items:center;gap:5px;line-height:16px}
  .service__list svg{flex:none}
  .city-panel{position:absolute;left:0;top:206px;width:378px;height:116px;
    background:linear-gradient(180deg,#bcd3e6 0%,#e8edf1 35%,#f4f4f2 70%,#ffffff 100%)}
  .card--back .brand{left:16px;top:228px}
  .card--back .brand__name{font-size:14px}
  .tagline{position:absolute;left:16px;top:264px;width:250px;font-style:italic;font-size:10.5px;line-height:12px;text-align:center}
  .contact-pill{position:absolute;left:12px;top:293px;height:20px;padding:0 8px;border-radius:5px;background:var(--orange);color:var(--white);
    display:flex;align-items:center;gap:5px;font-size:11.5px;white-space:nowrap}
  .contact-pill svg{flex:none}
  .seal{position:absolute;left:282px;top:232px;width:70px;height:70px;border-radius:50%;background:var(--seal);border:4px solid #e7e9ec}
  .back-web{position:absolute;left:52px;top:325px;font-size:15px;white-space:nowrap}
</style>
</head>
<body>

<section class="card card--front" aria-label="Postcard front">
  <div class="hero-photo" role="img" aria-label="Photo of a bright waterfront dining room with tall windows overlooking a bay"></div>
  <div class="hero-rule"></div>
  <div class="inset-photo" role="img" aria-label="Photo of a modern kitchen with pendant lights and a teal glass backsplash"></div>
  <h1 class="headline">Naples Commercial<br>and Real Estate Photography</h1>
  <div class="brand">
    <span class="brand__mark"></span>
    <span class="brand__name">Coral Coast Imaging<br>Real Estate Photography</span>
  </div>
  <div class="contact">
    <div>555-014-2290 &nbsp;|&nbsp; hello@coralcoastimaging.com</div>
    <div class="contact__web">www.coralcoastimaging.com</div>
  </div>
</section>

<section class="card card--back" aria-label="Postcard back">
  <div class="back-band"></div>
  <div class="back-band-ext"></div>
  <div class="gallery-photo gallery-photo--one" role="img" aria-label="Photo of an arched wine cellar doorway"></div>
  <div class="gallery-photo gallery-photo--two" role="img" aria-label="Photo of a curved staircase in a marble foyer"></div>
  <div class="stamp"></div>

  <p class="intro">Coral Coast Imaging serves Naples, Marco Island, Bonita Springs, Estero, Fort Myers and all of Southwest Florida.</p>

  <div class="service">
    <h2 class="service__title">Real Estate Photography</h2>
    <p>Quality high resolution imaging for real estate marketing using lighting and the latest editing techniques.</p>
    <ul class="service__list">
      <li><svg width="10" height="10" viewBox="0 0 10 10"><path d="M1 5.5l2.5 2.5L9 1.5" fill="none" stroke="#fff" stroke-width="2"/></svg>Hi Resolution Images</li>
      <li><svg width="10" height="10" viewBox="0 0 10 10"><path d="M1 5.5l2.5 2.5L9 1.5" fill="none" stroke="#fff" stroke-width="2"/></svg>Virtual Tours</li>
      <li><svg width="10" height="10" viewBox="0 0 10 10"><path d="M1 5.5l2.5 2.5L9 1.5" fill="none" stroke="#fff" stroke-width="2"/></svg>Fast &amp; Reliable Delivery</li>
    </ul>
  </div>

  <div class="city-panel" role="img" aria-label="Faded aerial photo of a coastal city skyline"></div>
  <div class="brand">
    <span class="brand__mark"></span>
    <span class="brand__name">Coral Coast Imaging<br>Real Estate Photography</span>
  </div>
  <p class="tagline">Contact us today for all of your Commercial Photography and Real Estate Photography needs</p>
  <div class="seal"></div>
  <div class="contact-pill">
    <svg width="11" height="11" viewBox="0 0 12 12"><path d="M2.5 1h2l1 3-1.5 1a7 7 0 0 0 3 3l1-1.5 3 1v2a1 1 0 0 1-1 1A10 10 0 0 1 1.5 2a1 1 0 0 1 1-1z" fill="#fff"/></svg>
    <span>555-014-2290</span>
    <span>|</span>
    <svg width="12" height="9" viewBox="0 0 12 9"><rect x=".5" y=".5" width="11" height="8" fill="none" stroke="#fff"/><path d="M.5 .5L6 5l5.5-4.5" fill="none" stroke="#fff"/></svg>
    <span>hello@coralcoastimaging.com</span>
  </div>
  <div class="back-web">www.coralcoastimaging.com</div>
</section>

</body>
</html>
```